Update PowerPoint Template Font & Color

We purchased a new PowerPoint template (attached) for our organization which needs to be updated with our color palette and fonts (also attached).

Please edit the master slides to reflect our fonts and udpate the graphic elements to reflect our color scheme.

NOTE: we do not want to change the slide background color (beige) or the dark blue accent color, those colors remain in the presentation template. All fonts must be large enough to be legible for a large presentation group at a conference.

```html
<!DOCTYPE html>
<html lang="en">
<head>
<meta charset="utf-8">
<title>Business Presentation Template – Brand Fonts Update</title>
<link href="https://fonts.googleapis.com/css2?family=Montserrat:wght@600;700;800&family=Open+Sans:wght@400;600&display=swap" rel="stylesheet">
<style>
:root{
  --beige:#e8e1d4;
  --sand:#d9ccb5;
  --tan:#c8b494;
  --navy:#0b2a52;
  --navy-2:#163c6e;
  --ink:#3a4654;
  --white:#ffffff;
  --line:#b9a88b;
}
*{box-sizing:border-box;margin:0;padding:0}
html,body{width:1200px;height:4724px;overflow:hidden;background:var(--white)}
.deck{display:grid;grid-template-columns:repeat(3,400px);grid-auto-rows:225px;width:1200px;height:4724px;overflow:hidden}
.slide{position:relative;overflow:hidden;background:var(--beige)}
.slide > *{position:absolute}
.navy{background:var(--navy)}
.sand{background:var(--sand)}
.tan{background:var(--tan)}
.white{background:var(--white)}
.title{font:700 15px/1.15 'Montserrat',sans-serif;color:var(--navy)}
.title.lg{font-size:18px}
.title.sm{font-size:11px}
.title.xs{font-size:8px}
.light{color:var(--white)}
.body{font:400 6.5px/1.45 'Open Sans',sans-serif;color:var(--ink)}
.body.light{color:#d8dfe9}
.label{font:700 6.5px/1.2 'Montserrat',sans-serif;color:var(--navy)}
.label.light{color:var(--white)}
.num{font:700 22px/1 'Montserrat',sans-serif;color:var(--navy)}
.ghost{font:700 34px/1 'Montserrat',sans-serif;color:var(--tan)}
.icon{width:24px;height:24px;border-radius:50%;border:1.5px solid var(--navy);display:grid;place-items:center}
.icon::after{content:"";width:8px;height:8px;border-radius:50%;background:var(--navy)}
.icon.fill{background:var(--navy)}
.icon.fill::after{background:var(--white)}
.icon.onnavy{border-color:var(--white)}
.icon.onnavy::after{background:var(--white)}
.portrait{border-radius:50%}
.photo-room{background:linear-gradient(135deg,#f1ebe1 0%,#ddc9aa 55%,#b99c76 100%)}
.photo-wood{background:linear-gradient(90deg,#c29f75,#e6d5ba 45%,#b48f63 80%,#d8c09c)}
.photo-city{background:linear-gradient(160deg,#1f4576 0%,#5d82ad 55%,#c5d2df 100%)}
.photo-person{background:linear-gradient(180deg,#cfd3d9 0%,#8a94a3 45%,#243a5a 100%)}
.photo-desk{background:linear-gradient(140deg,#f4efe7,#d8cbb6 60%,#9d8a70)}
.btn{font:600 5.5px/1 'Open Sans',sans-serif;color:var(--white);background:var(--navy);padding:3px 8px}
.btn.alt{background:var(--tan);color:var(--navy)}
.card{padding:10px 8px}
.rule{height:1px;background:var(--line)}
.letter{width:40px;height:40px;border-radius:50%;display:grid;place-items:center;font:800 18px/1 'Montserrat',sans-serif}
.vtext{writing-mode:vertical-rl;transform:rotate(180deg)}
.note{font:600 15px/1.6 'Montserrat',sans-serif;color:#1b1b1b}
</style>
</head>
<body>
<main class="deck">

<!-- Row 1 -->
<section class="slide white">
  <p class="note" style="left:48px;top:82px;width:320px">Changed Fonts To Your Brand Fonts<br>Increased Font Size</p>
</section>
<section class="slide">
  <div class="navy" style="left:0;top:0;width:150px;height:225px"></div>
  <div style="left:14px;top:14px;width:122px;height:86px;background:var(--navy-2);display:flex;align-items:center;gap:6px;padding:10px">
    <span style="width:12px;height:12px;background:var(--tan);flex:none"></span>
    <span class="title sm light">Norvale Expo 2026</span>
  </div>
  <p class="title sm light" style="left:40px;top:176px;width:90px">General<br>Session</p>
  <div class="icon" style="left:168px;top:44px"></div>
  <p class="label" style="left:204px;top:44px">Norvale Outlook 2026</p>
  <p class="body" style="left:204px;top:54px;width:180px">Short supporting text explains this point for the audience.</p>
  <div class="icon" style="left:168px;top:100px"></div>
  <p class="label" style="left:204px;top:100px">Lorem Ipsum Dolor</p>
  <p class="body" style="left:204px;top:110px;width:180px">Short supporting text explains this point for the audience.</p>
  <div class="icon" style="left:168px;top:156px"></div>
  <p class="label" style="left:204px;top:156px">Lorem Ipsum Dolor</p>
  <p class="body" style="left:204px;top:166px;width:180px">Short supporting text explains this point for the audience.</p>
</section>
<section class="slide">
  <p class="title sm vtext" style="left:22px;top:40px;height:120px">Your Business Presentation</p>
  <div class="photo-room" role="img" aria-label="Bright interior with wooden shelving and lamp" style="left:130px;top:20px;width:250px;height:160px"></div>
  <p class="body" style="left:130px;top:190px;width:250px">Short supporting text explains this point for the audience.</p>
</section>

<!-- Row 2 -->
<section class="slide">
  <div class="photo-desk" role="img" aria-label="Woman working at a laptop in a light office" style="left:0;top:0;width:200px;height:225px"></div>
  <div class="navy" style="left:200px;top:0;width:200px;height:225px"></div>
  <p class="title sm light" style="left:262px;top:50px;width:120px">Your Business Presentation</p>
  <p class="body light" style="left:262px;top:90px;width:110px">Short supporting text explains this point for the audience. Short supporting text explains this point.</p>
</section>
<section class="slide">
  <div class="tan card" style="left:26px;top:50px;width:104px;height:140px"></div>
  <div class="navy card" style="left:148px;top:36px;width:104px;height:160px"></div>
  <div class="tan card" style="left:270px;top:50px;width:104px;height:140px"></div>
  <p class="label" style="left:52px;top:60px">Name Package</p><p class="num" style="left:52px;top:74px">$99</p>
  <p class="body" style="left:52px;top:102px;width:70px">Lorem ipsum dolor<br>Lorem ipsum dolor<br>Lorem ipsum dolor<br>Lorem ipsum dolor</p>
  <span class="btn" style="left:52px;top:172px">Get This Plan</span>
  <p class="label light" style="left:174px;top:48px">Name Package</p><p class="num light" style="left:174px;top:62px">$99</p>
  <p class="body light" style="left:174px;top:92px;width:70px">Lorem ipsum dolor<br>Lorem ipsum dolor<br>Lorem ipsum dolor<br>Lorem ipsum dolor</p>
  <span class="btn alt" style="left:174px;top:176px">Get This Plan</span>
  <p class="label" style="left:296px;top:60px">Name Package</p><p class="num" style="left:296px;top:74px">$99</p>
  <p class="body" style="left:296px;top:102px;width:70px">Lorem ipsum dolor<br>Lorem ipsum dolor<br>Lorem ipsum dolor<br>Lorem ipsum dolor</p>
  <span class="btn" style="left:296px;top:172px">Get This Plan</span>
</section>
<section class="slide">
  <div class="sand" style="left:26px;top:46px;width:104px;height:150px"></div>
  <div class="sand" style="left:148px;top:36px;width:104px;height:160px"></div>
  <div class="sand" style="left:270px;top:46px;width:104px;height:150px"></div>
  <p class="label" style="left:52px;top:56px">Name Package</p><p class="num" style="left:52px;top:70px">$99</p>
  <p class="body" style="left:52px;top:98px">Lorem ipsum dolor<br>Lorem ipsum dolor<br>Lorem ipsum dolor</p>
  <span class="btn" style="left:26px;top:180px;width:104px;text-align:center">Get This Plan</span>
  <p class="label" style="left:174px;top:46px">Name Package</p><p class="num" style="left:174px;top:60px">$99</p>
  <p class="body" style="left:174px;top:88px">Lorem ipsum dolor<br>Lorem ipsum dolor<br>Lorem ipsum dolor</p>
  <span class="btn" style="left:148px;top:180px;width:104px;text-align:center">Get This Plan</span>
  <p class="label" style="left:296px;top:56px">Name Package</p><p class="num" style="left:296px;top:70px">$99</p>
  <p class="body" style="left:296px;top:98px">Lorem ipsum dolor<br>Lorem ipsum dolor<br>Lorem ipsum dolor</p>
  <span class="btn" style="left:270px;top:180px;width:104px;text-align:center">Get This Plan</span>
</section>

<!-- Row 3 -->
<section class="slide navy">
  <div class="photo-wood" role="img" aria-label="Wooden slatted wall with a bench" style="left:36px;top:24px;width:340px;height:100px"></div>
  <div class="icon onnavy" style="left:44px;top:142px"></div>
  <p class="title sm light" style="left:156px;top:140px">Add Your Title</p>
  <p class="body light" style="left:156px;top:158px;width:190px">Short supporting text explains this point for the audience. Short supporting text explains this point.</p>
</section>
<section class="slide navy">
  <p class="title sm light" style="left:28px;top:20px">Contents</p>
  <p class="body light" style="left:28px;top:34px">Description Here</p>
  <div class="icon onnavy" style="left:28px;top:76px"></div><p class="label light" style="left:60px;top:76px">Add Your Title</p><p class="body light" style="left:60px;top:86px;width:120px">Short supporting text explains this point.</p>
  <div class="icon onnavy" style="left:214px;top:76px"></div><p class="label light" style="left:246px;top:76px">Add Your Title</p><p class="body light" style="left:246px;top:86px;width:120px">Short supporting text explains this point.</p>
  <div class="icon onnavy" style="left:28px;top:136px"></div><p class="label light" style="left:60px;top:136px">Add Your Title</p><p class="body light" style="left:60px;top:146px;width:120px">Short supporting text explains this point.</p>
  <div class="icon onnavy" style="left:214px;top:136px"></div><p class="label light" style="left:246px;top:136px">Add Your Title</p><p class="body light" style="left:246px;top:146px;width:120px">Short supporting text explains this point.</p>
</section>
<section class="slide">
  <div class="navy" style="left:0;top:0;width:130px;height:225px"></div>
  <p class="title sm light" style="left:28px;top:30px">About Us</p>
  <p class="body light" style="left:28px;top:44px">Description Here</p>
  <p class="body light" style="left:28px;top:120px;width:90px">Short supporting text explains this point for the audience.</p>
  <p class="label light" style="left:28px;top:190px">Company Name</p>
  <div class="photo-room" role="img" aria-label="Vase with dried branches on a shelf" style="left:138px;top:36px;width:100px;height:130px"></div>
  <p class="ghost" style="left:272px;top:36px;font-size:20px">01</p>
  <p class="label" style="left:272px;top:60px">Add Your Title</p><p class="body" style="left:272px;top:70px;width:110px">Short supporting text explains this point.</p>
  <p class="ghost" style="left:272px;top:106px;font-size:20px">02</p>
  <p class="label" style="left:272px;top:130px">Add Your Title</p><p class="body" style="left:272px;top:140px;width:110px">Short supporting text explains this point.</p>
</section>

<!-- Row 4 -->
<section class="slide">
  <div class="navy" style="left:0;top:0;width:182px;height:225px"></div>
  <p class="title sm light" style="left:28px;top:36px">Add Your Title</p>
  <p class="body light" style="left:28px;top:52px">Description Here</p>
  <p class="body light" style="left:28px;top:80px;width:130px">Short supporting text explains this point for the audience. Short supporting text explains this point for the audience.</p>
  <div class="navy" style="left:220px;top:36px;width:64px;height:72px"></div><div class="navy" style="left:300px;top:36px;width:64px;height:72px"></div>
  <div class="sand" style="left:220px;top:120px;width:64px;height:72px"></div><div class="navy" style="left:300px;top:120px;width:64px;height:72px"></div>
  <p class="body light" style="left:226px;top:64px;width:52px">Short text explains this.</p>
  <p class="body light" style="left:306px;top:64px;width:52px">Short text explains this.</p>
  <p class="body" style="left:226px;top:148px;width:52px">Short text explains this.</p>
  <p class="body light" style="left:306px;top:148px;width:52px">Short text explains this.</p>
</section>
<section class="slide">
  <div class="navy" style="left:34px;top:36px;width:64px;height:72px"></div><div class="sand" style="left:114px;top:36px;width:64px;height:72px"></div>
  <div class="navy" style="left:34px;top:120px;width:64px;height:72px"></div><div class="navy" style="left:114px;top:120px;width:64px;height:72px"></div>
  <p class="body light" style="left:40px;top:64px;width:52px">Short text explains this.</p>
  <p class="body" style="left:120px;top:64px;width:52px">Short text explains this.</p>
  <p class="body light" style="left:40px;top:148px;width:52px">Short text explains this.</p>
  <p class="body light" style="left:120px;top:148px;width:52px">Short text explains this.</p>
  <div class="navy" style="left:210px;top:0;width:190px;height:225px"></div>
  <p class="title sm light" style="left:230px;top:36px">Add Your Title</p>
  <p class="body light" style="left:230px;top:52px">Description Here</p>
  <p class="body light" style="left:230px;top:80px;width:140px">Short supporting text explains this point for the audience. Short supporting text explains this point for the audience.</p>
</section>
<section class="slide">
  <div class="navy" style="left:0;top:0;width:400px;height:100px"></div>
  <p class="title sm light" style="left:28px;top:26px;width:200px">Quote Lorem Ipsum Dolor sit Amet, consectu Labore et dolore</p>
  <p class="label" style="left:28px;top:126px">Add Your Title</p>
  <p class="body" style="left:28px;top:138px;width:120px">Short supporting text explains this point for the audience.</p>
  <div class="sand" style="left:160px;top:84px;width:90px;height:110px"></div>
  <div class="navy" style="left:270px;top:84px;width:90px;height:110px"></div>
  <div class="icon" style="left:193px;top:96px"></div><p class="body" style="left:168px;top:130px;width:74px">Short supporting text explains this point.</p>
  <div class="icon onnavy" style="left:303px;top:96px"></div><p class="body light" style="left:278px;top:130px;width:74px">Short supporting text explains this point.</p>
</section>

<!-- Row 5 -->
<section class="slide">
  <p class="title sm" style="left:150px;top:16px;width:140px;text-align:center">Your Business Presentation</p>
  <svg style="left:40px;top:70px" width="320" height="80" viewBox="0 0 320 80">
    <g fill="none" stroke-width="10">
      <circle cx="50" cy="40" r="30" stroke="var(--sand)"/><circle cx="50" cy="40" r="30" stroke="var(--navy)" stroke-dasharray="83 189" transform="rotate(-90 50 40)"/>
      <circle cx="160" cy="40" r="30" stroke="var(--sand)"/><circle cx="160" cy="40" r="30" stroke="var(--navy)" stroke-dasharray="83 189" transform="rotate(-90 160 40)"/>
      <circle cx="270" cy="40" r="30" stroke="var(--sand)"/><circle cx="270" cy="40" r="30" stroke="var(--navy)" stroke-dasharray="83 189" transform="rotate(-90 270 40)"/>
    </g>
    <g font-family="Montserrat,sans-serif" font-weight="700" font-size="7" fill="var(--navy)">
      <text x="10" y="14">44%</text><text x="120" y="14">44%</text><text x="230" y="14">44%</text>
      <text x="80" y="76">54%</text><text x="190" y="76">54%</text><text x="300" y="76">54%</text>
      <text x="38" y="43">Your Title</text><text x="148" y="43">Your Title</text><text x="258" y="43">Your Title</text>
    </g>
  </svg>
  <p class="body" style="left:80px;top:180px;width:240px;text-align:center">Short supporting text explains this point for the audience. Short supporting text explains this point.</p>
</section>
<section class="slide">
  <p class="title sm" style="left:26px;top:36px">Add Your Title</p>
  <p class="body" style="left:26px;top:50px">Description Here</p>
  <p class="body" style="left:26px;top:74px;width:100px">Short supporting text explains this point for the audience.</p>
  <span class="btn" style="left:26px;top:180px">www.website.com</span>
  <svg style="left:150px;top:30px" width="120" height="170" viewBox="0 0 120 170"><path d="M90 10 A80 80 0 0 0 90 160" fill="none" stroke="var(--line)" stroke-width="1"/></svg>
  <div class="icon" style="left:238px;top:34px"></div><div class="icon fill" style="left:186px;top:100px"></div><div class="icon" style="left:238px;top:166px"></div>
  <p class="label" style="left:272px;top:34px">Lorem Ipsum Dolor</p><p class="body" style="left:272px;top:44px;width:110px">Short supporting text explains this point.</p>
  <p class="label" style="left:220px;top:100px">Lorem Ipsum Dolor</p><p class="body" style="left:220px;top:110px;width:110px">Short supporting text explains this point.</p>
  <p class="label" style="left:272px;top:166px">Lorem Ipsum Dolor</p><p class="body" style="left:272px;top:176px;width:110px">Short supporting text explains this point.</p>
</section>
<section class="slide">
  <div class="navy" style="left:0;top:0;width:42px;height:225px"></div>
  <p class="title sm light vtext" style="left:14px;top:40px;height:140px">Add Your Title</p>
  <svg style="left:175px;top:70px" width="80" height="80" viewBox="0 0 80 80">
    <path d="M40 40 L40 0 A40 40 0 0 1 80 40Z" fill="var(--navy)"/><path d="M40 40 L80 40 A40 40 0 0 1 40 80Z" fill="var(--tan)"/>
    <path d="M40 40 L40 80 A40 40 0 0 1 0 40Z" fill="var(--navy)"/><path d="M40 40 L0 40 A40 40 0 0 1 40 0Z" fill="var(--tan)"/>
  </svg>
  <p class="label" style="left:80px;top:36px">Lorem Ipsum Dolor</p><p class="body" style="left:80px;top:46px;width:84px">Short supporting text explains this point.</p>
  <p class="label" style="left:80px;top:136px">Lorem Ipsum Dolor</p><p class="body" style="left:80px;top:146px;width:84px">Short supporting text explains this point.</p>
  <p class="label" style="left:286px;top:36px">Lorem Ipsum Dolor</p><p class="body" style="left:286px;top:46px;width:84px">Short supporting text explains this point.</p>
  <p class="label" style="left:286px;top:136px">Lorem Ipsum Dolor</p><p class="body" style="left:286px;top:146px;width:84px">Short supporting text explains this point.</p>
</section>

<!-- Row 6 -->
<section class="slide navy">
  <p class="title sm light" style="left:0;top:26px;width:400px;text-align:center">Our Team</p>
  <p class="body light" style="left:100px;top:42px;width:200px;text-align:center">Short supporting text explains this point for the audience.</p>
  <div class="photo-person portrait" role="img" aria-label="Team member portrait" style="left:54px;top:84px;width:46px;height:46px"></div>
  <div class="photo-person portrait" role="img" aria-label="Team member portrait" style="left:136px;top:84px;width:46px;height:46px"></div>
  <div class="photo-person portrait" role="img" aria-label="Team member portrait" style="left:218px;top:84px;width:46px;height:46px"></div>
  <div class="photo-person portrait" role="img" aria-label="Team member portrait" style="left:300px;top:84px;width:46px;height:46px"></div>
  <p class="label light" style="left:50px;top:144px;width:54px;text-align:center">Name Here</p>
  <p class="label light" style="left:132px;top:144px;width:54px;text-align:center">Name Here</p>
  <p class="label light" style="left:214px;top:144px;width:54px;text-align:center">Name Here</p>
  <p class="label light" style="left:296px;top:144px;width:54px;text-align:center">Name Here</p>
  <p class="body light" style="left:40px;top:160px;width:320px;display:flex;justify-content:space-between"><span style="width:70px">Short text explains this point.</span><span style="width:70px">Short text explains this point.</span><span style="width:70px">Short text explains this point.</span><span style="width:70px">Short text explains this point.</span></p>
</section>
<section class="slide">
  <p class="title" style="left:34px;top:30px">Add Your Title</p>
  <p class="body" style="left:34px;top:50px">Description Here</p>
  <p class="body" style="left:34px;top:80px;width:110px">Short supporting text explains this point for the audience. Short supporting text explains.</p>
  <div class="navy" style="left:0;top:180px;width:400px;height:45px"></div>
  <div class="photo-person" role="img" aria-label="Man in a suit" style="left:200px;top:20px;width:120px;height:205px"></div>
  <div class="icon onnavy" style="left:36px;top:190px"></div>
  <p class="label light" style="left:68px;top:192px">Lorem Ipsum Dolor</p>
  <div class="icon" style="left:340px;top:40px"></div><div class="icon fill" style="left:170px;top:104px"></div>
</section>
<section class="slide navy">
  <div class="photo-wood" role="img" aria-label="Lobby with wooden wall and plant" style="left:0;top:0;width:200px;height:225px"></div>
  <p class="title light" style="left:254px;top:40px;width:120px">Add Your Title Here</p>
  <p class="body light" style="left:254px;top:84px;width:120px">Short supporting text explains this point for the audience. Short supporting text explains this point for the audience.</p>
  <span class="btn alt" style="left:300px;top:180px">www.website.com</span>
</section>

<!-- Row 7 -->
<section class="slide">
  <p class="title sm" style="left:0;top:24px;width:400px;text-align:center">Our Team</p>
  <p class="body" style="left:110px;top:40px;width:180px;text-align:center">Short supporting text explains this point.</p>
  <div class="navy" style="left:0;top:100px;width:400px;height:125px"></div>
  <div class="photo-person portrait" role="img" aria-label="Team member portrait" style="left:82px;top:74px;width:52px;height:52px"></div>
  <div class="photo-person portrait" role="img" aria-label="Team member portrait" style="left:174px;top:74px;width:52px;height:52px"></div>
  <div class="photo-person portrait" role="img" aria-label="Team member portrait" style="left:266px;top:74px;width:52px;height:52px"></div>
  <p class="label light" style="left:78px;top:140px;width:60px;text-align:center">Name Here</p>
  <p class="label light" style="left:170px;top:140px;width:60px;text-align:center">Name Here</p>
  <p class="label light" style="left:262px;top:140px;width:60px;text-align:center">Name Here</p>
  <p class="body light" style="left:66px;top:156px;width:84px;text-align:center">Short text explains this point.</p>
  <p class="body light" style="left:158px;top:156px;width:84px;text-align:center">Short text explains this point.</p>
  <p class="body light" style="left:250px;top:156px;width:84px;text-align:center">Short text explains this point.</p>
</section>
<section class="slide">
  <div class="photo-city" role="img" aria-label="Glass office tower against blue sky" style="left:0;top:0;width:170px;height:225px"></div>
  <div class="sand" style="left:170px;top:0;width:230px;height:60px"></div>
  <p class="title sm" style="left:188px;top:26px">Add Your Title</p>
  <p class="body" style="left:188px;top:40px;width:190px">Short supporting text explains this point.</p>
  <div class="icon" style="left:188px;top:100px"></div><p class="label" style="left:220px;top:100px">Lorem Ipsum Dolor</p><p class="body" style="left:220px;top:110px;width:150px">Short supporting text explains this point.</p>
  <div class="icon" style="left:188px;top:150px"></div><p class="label" style="left:220px;top:150px">Lorem Ipsum Dolor</p><p class="body" style="left:220px;top:160px;width:150px">Short supporting text explains this point.</p>
</section>
<section class="slide">
  <div class="navy" style="left:200px;top:0;width:200px;height:225px"></div>
  <p class="title sm" style="left:64px;top:44px;width:90px">Add Your Title Here</p>
  <p class="body" style="left:24px;top:84px;width:150px">Short supporting text explains this point for the audience. Short supporting text explains this point.</p>
  <span class="btn" style="left:64px;top:180px">www.website.com</span>
  <p class="title sm light" style="left:264px;top:44px;width:90px">Add Your Title Here</p>
  <p class="body light" style="left:224px;top:84px;width:150px">Short supporting text explains this point for the audience. Short supporting text explains this point.</p>
  <span class="btn alt" style="left:264px;top:180px">www.website.com</span>
</section>

<!-- Row 8 -->
<section class="slide">
  <div class="photo-city" role="img" aria-label="Modern office building facade" style="left:160px;top:0;width:240px;height:225px;clip-path:polygon(40% 0,100% 0,100% 100%,0 100%)"></div>
  <p class="title" style="left:26px;top:40px">Add Your Title</p>
  <p class="body" style="left:26px;top:60px">Description Here</p>
  <p class="body" style="left:26px;top:90px;width:110px">Short supporting text explains this point for the audience. Short supporting text explains this point for the audience.</p>
</section>
<section class="slide">
  <div class="tan" style="left:40px;top:40px;width:90px;height:8px"></div><div class="navy" style="left:154px;top:40px;width:90px;height:8px"></div><div class="tan" style="left:268px;top:40px;width:90px;height:8px"></div>
  <p class="label" style="left:60px;top:42px;font-size:5px">Add Your Title</p><p class="label light" style="left:174px;top:42px;font-size:5px">Add Your Title</p><p class="label" style="left:288px;top:42px;font-size:5px">Add Your Title</p>
  <p class="body" style="left:40px;top:60px;width:90px">Short supporting text explains this point.</p>
  <p class="body" style="left:154px;top:60px;width:90px">Short supporting text explains this point.</p>
  <p class="body" style="left:268px;top:60px;width:90px">Short supporting text explains this point.</p>
  <div class="navy" style="left:0;top:120px;width:400px;height:105px"></div>
  <p class="title sm light" style="left:0;top:158px;width:400px;text-align:center">Your Business Presentation</p>
  <p class="body light" style="left:0;top:176px;width:400px;text-align:center;letter-spacing:3px">EXAMPLE</p>
</section>
<section class="slide">
  <div style="left:18px;top:14px;width:364px;height:200px;border:1.5px solid var(--navy)"></div>
  <p class="title sm" style="left:60px;top:30px;width:120px">Your Business Presentation</p>
  <svg style="left:40px;top:80px" width="320" height="120" viewBox="0 0 320 120">
    <g fill="none" stroke-width="12">
      <path d="M10 100 A40 40 0 0 1 90 100" stroke="var(--sand)"/><path d="M10 100 A40 40 0 0 1 30 66" stroke="var(--navy)"/>
      <path d="M95 60 A40 40 0 0 0 175 60" stroke="var(--navy)"/>
      <path d="M160 100 A40 40 0 0 1 240 100" stroke="var(--sand)"/><path d="M160 100 A40 40 0 0 1 230 74" stroke="var(--navy)"/>
      <path d="M245 60 A40 40 0 0 0 315 60" stroke="var(--navy)"/>
    </g>
    <g font-family="Montserrat,sans-serif" font-weight="700" font-size="9" fill="var(--navy)">
      <text x="36" y="98">20%</text><text x="122" y="70">40%</text><text x="186" y="98">80%</text><text x="268" y="70">40%</text>
    </g>
  </svg>
  <p class="label" style="left:140px;top:74px">Lorem Ipsum</p><p class="label" style="left:290px;top:74px">Lorem Ipsum</p>
  <p class="body" style="left:60px;top:156px;width:70px">Short text explains this point.</p>
  <p class="body" style="left:210px;top:156px;width:70px">Short text explains this point.</p>
</section>

<!-- Row 9 -->
<section class="slide">
  <div class="navy" style="left:0;top:0;width:400px;height:110px"></div>
  <p class="title sm light" style="left:36px;top:26px;width:120px">Your Business Presentation</p>
  <div class="icon onnavy" style="left:58px;top:84px;background:var(--beige)"></div><div class="icon onnavy" style="left:146px;top:84px;background:var(--beige)"></div>
  <div class="icon onnavy" style="left:234px;top:84px;background:var(--beige)"></div><div class="icon onnavy" style="left:322px;top:84px;background:var(--beige)"></div>
  <p class="label" style="left:36px;top:126px">Lorem Ipsum Dolor</p><p class="label" style="left:124px;top:126px">Lorem Ipsum Dolor</p><p class="label" style="left:212px;top:126px">Lorem Ipsum Dolor</p><p class="label" style="left:300px;top:126px">Lorem Ipsum Dolor</p>
  <p class="body" style="left:36px;top:140px;width:70px">Short supporting text explains this point.</p>
  <p class="body" style="left:124px;top:140px;width:70px">Short supporting text explains this point.</p>
  <p class="body" style="left:212px;top:140px;width:70px">Short supporting text explains this point.</p>
  <p class="body" style="left:300px;top:140px;width:70px">Short supporting text explains this point.</p>
</section>
<section class="slide">
  <p class="title sm" style="left:36px;top:22px;width:120px">Your Business Presentation</p>
  <div class="rule" style="left:40px;top:128px;width:320px;background:var(--navy)"></div>
  <div class="icon fill" style="left:92px;top:100px"></div><div class="icon" style="left:226px;top:100px"></div>
  <div class="icon fill" style="left:144px;top:152px"></div><div class="icon fill" style="left:312px;top:152px"></div>
  <p class="label" style="left:130px;top:74px">Add Your Title</p><p class="body" style="left:110px;top:84px;width:90px">Short text explains this point.</p>
  <p class="label" style="left:290px;top:74px">Add Your Title</p><p class="body" style="left:270px;top:84px;width:90px">Short text explains this point.</p>
  <p class="label" style="left:40px;top:148px">Add Your Title</p><p class="body" style="left:30px;top:158px;width:90px">Short text explains this point.</p>
  <p class="label" style="left:210px;top:148px">Add Your Title</p><p class="body" style="left:200px;top:158px;width:90px">Short text explains this point.</p>
</section>
<section class="slide">
  <div class="navy" style="left:0;top:140px;width:400px;height:85px"></div>
  <div class="photo-desk" role="img" aria-label="Person working at a desk" style="left:30px;top:20px;width:70px;height:100px"></div>
  <div class="photo-desk" role="img" aria-label="Person working at a laptop" style="left:116px;top:20px;width:70px;height:100px"></div>
  <span class="label light" style="left:22px;top:14px;background:var(--navy);padding:3px">01</span><span class="label light" style="left:108px;top:14px;background:var(--navy);padding:3px">02</span>
  <p class="body light" style="left:30px;top:156px;width:70px">Short text explains this point.</p>
  <p class="body light" style="left:116px;top:156px;width:70px">Short text explains this point.</p>
  <p class="title sm" style="left:214px;top:34px">Add Your Title</p>
  <p class="body" style="left:214px;top:50px;width:160px">Short supporting text explains this point for the audience.</p>
  <div class="photo-room" role="img" aria-label="Shelf with books and a lamp" style="left:214px;top:90px;width:160px;height:100px"></div>
</section>

<!-- Row 10 -->
<section class="slide">
  <p class="title sm" style="left:26px;top:30px;width:120px">Your Business Presentation</p>
  <p class="body" style="left:26px;top:62px;width:160px">Short supporting text explains this point for the audience.</p>
  <div class="navy" style="left:0;top:130px;width:270px;height:95px"></div>
  <div class="photo-room" role="img" aria-label="Vase and books on a shelf" style="left:270px;top:0;width:130px;height:225px"></div>
  <div class="sand" style="left:10px;top:138px;width:110px;height:80px"></div>
  <p class="label" style="left:20px;top:148px">Add Your Title</p><p class="body" style="left:20px;top:160px;width:90px">Short text explains this point.</p>
  <p class="label light" style="left:150px;top:148px">Add Your Title</p><p class="body light" style="left:150px;top:160px;width:90px">Short text explains this point.</p>
</section>
<section class="slide">
  <p class="title sm" style="left:30px;top:28px;width:120px">Your Business Presentation</p>
  <p class="body" style="left:30px;top:60px;width:140px">Short supporting text explains this point.</p>
  <div class="photo-wood" role="img" aria-label="Warm wooden slatted panel" style="left:0;top:100px;width:240px;height:125px"></div>
  <div class="navy" style="left:240px;top:0;width:160px;height:225px"></div>
  <div class="icon onnavy" style="left:254px;top:40px"></div><p class="label light" style="left:286px;top:40px">Add Title Here</p><p class="body light" style="left:286px;top:52px;width:100px">Short supporting text explains this point.</p>
  <div class="icon onnavy" style="left:254px;top:116px"></div><p class="label light" style="left:286px;top:116px">Add Title Here</p><p class="body light" style="left:286px;top:128px;width:100px">Short supporting text explains this point.</p>
</section>
<section class="slide">
  <p class="title sm" style="left:0;top:24px;width:400px;text-align:center">Your Business Presentation</p>
  <div class="photo-wood" role="img" aria-label="Slatted wooden wall texture" style="left:0;top:50px;width:400px;height:120px"></div>
  <p class="body" style="left:40px;top:180px;width:320px;text-align:center">Short supporting text explains this point for the audience. Short supporting text explains this point for the audience.</p>
</section>

<!-- Row 11 -->
<section class="slide">
  <div class="navy" style="left:250px;top:150px;width:150px;height:75px"></div>
  <div class="photo-person" role="img" aria-label="Businessman pointing forward" style="left:250px;top:10px;width:140px;height:215px"></div>
  <p class="title sm" style="left:26px;top:24px;width:120px">Your Business Presentation</p>
  <p class="body" style="left:26px;top:56px;width:130px">Short supporting text explains this point for the audience.</p>
  <div class="icon" style="left:40px;top:110px"></div><div class="icon" style="left:120px;top:110px"></div>
  <p class="label" style="left:36px;top:142px;font-size:8px">+6000</p><p class="label" style="left:116px;top:142px;font-size:8px">+6000</p>
  <p class="body" style="left:26px;top:156px;width:60px">Short text explains this point.</p>
  <p class="body" style="left:106px;top:156px;width:60px">Short text explains this point.</p>
</section>
<section class="slide">
  <div class="photo-desk" role="img" aria-label="Notebook and coffee on a desk" style="left:30px;top:26px;width:110px;height:64px"></div>
  <div class="photo-room" role="img" aria-label="Interior with wooden shelves" style="left:30px;top:122px;width:110px;height:64px"></div>
  <p class="label" style="left:178px;top:30px">Add Your Title</p><p class="body" style="left:178px;top:42px;width:110px">Short supporting text explains this point.</p>
  <p class="label" style="left:178px;top:126px">Add Your Title</p><p class="body" style="left:178px;top:138px;width:110px">Short supporting text explains this point.</p>
  <div class="navy" style="left:326px;top:0;width:44px;height:225px"></div>
  <p class="title sm light vtext" style="left:338px;top:40px;height:150px;transform:none">Your Business Presentation</p>
</section>
<section class="slide">
  <p class="title sm" style="left:36px;top:24px;width:120px">Your Business Presentation</p>
  <svg style="left:36px;top:66px" width="330" height="140" viewBox="0 0 330 140">
    <g fill="var(--navy)"><rect x="0" y="0" width="52" height="12"/><rect x="55" y="0" width="52" height="12"/><rect x="110" y="0" width="52" height="12"/><rect x="165" y="0" width="52" height="12"/><rect x="220" y="0" width="52" height="12"/><rect x="275" y="0" width="52" height="12"/></g>
    <g fill="var(--sand)">
      <rect x="0" y="16" width="327" height="14"/><rect x="0" y="50" width="327" height="14"/><rect x="0" y="84" width="327" height="14"/>
    </g>
    <g font-family="Open Sans,sans-serif" font-size="5.5" fill="var(--ink)">
      <text x="4" y="26">Description</text><text x="59" y="26">Description</text><text x="114" y="26">Description</text><text x="169" y="26">Description</text><text x="224" y="26">Description</text><text x="279" y="26">Description</text>
      <text x="4" y="43">Description</text><text x="59" y="43">Description</text><text x="114" y="43">Description</text><text x="169" y="43">Description</text><text x="224" y="43">Description</text><text x="279" y="43">Description</text>
      <text x="4" y="60">Description</text><text x="59" y="60">Description</text><text x="114" y="60">Description</text><text x="169" y="60">Description</text><text x="224" y="60">Description</text><text x="279" y="60">Description</text>
      <text x="4" y="77">Description</text><text x="59" y="77">Description</text><text x="114" y="77">Description</text><text x="169" y="77">Description</text><text x="224" y="77">Description</text><text x="279" y="77">Description</text>
      <text x="4" y="94">Description</text><text x="59" y="94">Description</text><text x="114" y="94">Description</text><text x="169" y="94">Description</text><text x="224" y="94">Description</text><text x="279" y="94">Description</text>
    </g>
    <g font-family="Montserrat,sans-serif" font-weight="700" font-size="5.5" fill="#fff">
      <text x="4" y="8">Lorem Ipsum</text><text x="59" y="8">Lorem Ipsum</text><text x="114" y="8">Lorem Ipsum</text><text x="169" y="8">Lorem Ipsum</text><text x="224" y="8">Lorem Ipsum</text><text x="279" y="8">Lorem Ipsum</text>
    </g>
  </svg>
</section>

<!-- Row 12 -->
<section class="slide">
  <div class="photo-wood" role="img" aria-label="Wooden wall detail" style="left:210px;top:0;width:190px;height:225px;clip-path:polygon(0 0,100% 0,100% 100%,40% 100%)"></div>
  <svg style="left:190px;top:120px" width="120" height="105" viewBox="0 0 120 105"><polygon points="60,0 120,105 0,105" fill="var(--navy)"/></svg>
  <svg style="left:140px;top:0" width="140" height="80" viewBox="0 0 140 80"><polygon points="0,0 140,0 70,80" fill="var(--tan)"/></svg>
  <p class="title sm" style="left:34px;top:40px;width:100px">Add Your Title Here</p>
  <p class="body" style="left:34px;top:90px;width:150px">Short supporting text explains this point for the audience. Short supporting text explains this point for the audience.</p>
  <span class="btn" style="left:34px;top:180px">www.website.com</span>
</section>
<section class="slide">
  <p class="title sm" style="left:34px;top:30px;width:100px">Add Your Title Here</p>
  <p class="body" style="left:34px;top:90px;width:150px">Short supporting text explains this point for the audience. Short supporting text explains this point for the audience.</p>
  <div class="icon" style="left:34px;top:170px"></div><p class="num" style="left:64px;top:172px;font-size:16px">+72.000</p>
  <svg style="left:200px;top:0" width="200" height="225" viewBox="0 0 200 225"><polygon points="60,0 200,0 200,225 60,225 0,112" fill="var(--navy)"/></svg>
  <div class="photo-person" role="img" aria-label="Man in suit holding a coffee cup" style="left:250px;top:0;width:150px;height:225px;clip-path:polygon(30% 0,100% 0,100% 100%,30% 100%,0 50%)"></div>
</section>
<section class="slide">
  <div class="navy" style="left:0;top:140px;width:400px;height:85px"></div>
  <div class="photo-city" role="img" aria-label="Phone screen showing office towers" style="left:24px;top:20px;width:70px;height:150px;border-radius:10px;border:4px solid var(--navy)"></div>
  <p class="title sm" style="left:190px;top:24px">Add Your Title Here</p>
  <p class="body" style="left:190px;top:42px;width:180px">Short supporting text explains this point for the audience. Short supporting text explains this point.</p>
  <p class="label light" style="left:190px;top:156px">Title 1</p><p class="body light" style="left:190px;top:168px;width:80px">Short text explains this point.</p>
  <p class="label light" style="left:290px;top:156px">Title 2</p><p class="body light" style="left:290px;top:168px;width:80px">Short text explains this point.</p>
  <span class="btn alt" style="left:310px;top:204px">www.website.com</span>
</section>

<!-- Row 13 -->
<section class="slide">
  <div class="tan" style="left:0;top:0;width:160px;height:120px"></div>
  <div class="navy" style="left:0;top:120px;width:400px;height:105px"></div>
  <p class="title sm" style="left:150px;top:30px;width:120px">Your Business Presentation</p>
  <div class="photo-city" role="img" aria-label="Laptop showing a glass office tower" style="left:118px;top:66px;width:160px;height:100px;border:4px solid #222"></div>
  <p class="label light" style="left:28px;top:140px">Add Your Title</p><p class="body light" style="left:28px;top:152px;width:80px">Short text explains this point.</p>
  <p class="label light" style="left:300px;top:140px">Add Your Title</p><p class="body light" style="left:300px;top:152px;width:80px">Short text explains this point.</p>
</section>
<section class="slide">
  <p class="title sm" style="left:30px;top:30px;width:100px">Add Your Title Here</p>
  <p class="body" style="left:30px;top:70px;width:150px">Short supporting text explains this point for the audience. Short supporting text explains this point for the audience.</p>
  <span class="btn" style="left:30px;top:170px">www.website.com</span>
  <div class="photo-desk" role="img" aria-label="Woman working at a desk" style="left:220px;top:40px;width:90px;height:60px"></div>
  <div class="photo-desk" role="img" aria-label="Open notebook on a table" style="left:220px;top:120px;width:150px;height:80px"></div>
  <p class="ghost" style="left:320px;top:50px">02</p>
</section>
<section class="slide navy">
  <div class="photo-city" role="img" aria-label="City skyline with office buildings" style="left:0;top:0;width:400px;height:70px"></div>
  <div class="photo-person" role="img" aria-label="Businessman with thumbs up" style="left:30px;top:30px;width:120px;height:195px"></div>
  <p class="title sm light" style="left:200px;top:84px">Your Name</p><p class="body light" style="left:200px;top:100px">Position</p>
  <p class="label light" style="left:200px;top:130px">Lorem Ipsum Dolor</p>
  <p class="body light" style="left:200px;top:142px;width:150px">Short supporting text explains this point for the audience.</p>
  <span class="btn alt" style="left:200px;top:186px">www.website.com</span>
  <div class="tan" style="left:360px;top:150px;width:40px;height:75px"></div>
</section>

<!-- Row 14 -->
<section class="slide">
  <div class="photo-room" role="img" aria-label="Room with pendant lamps and shelves" style="left:0;top:0;width:180px;height:225px"></div>
  <p class="ghost" style="left:20px;top:30px;color:var(--white)">01</p>
  <div class="navy" style="left:0;top:140px;width:40px;height:85px"></div>
  <p class="title sm" style="left:216px;top:40px;width:100px">Add Your Title Here</p>
  <p class="body" style="left:216px;top:80px;width:160px">Short supporting text explains this point for the audience. Short supporting text explains this point for the audience.</p>
  <span class="btn" style="left:216px;top:170px">www.website.com</span>
</section>
<section class="slide">
  <p class="title sm" style="left:36px;top:22px;width:120px">Your Business Presentation</p>
  <svg style="left:36px;top:72px" width="330" height="60" viewBox="0 0 330 60">
    <g fill="none" stroke-width="5">
      <circle cx="30" cy="30" r="24" stroke="var(--sand)"/><circle cx="30" cy="30" r="24" stroke="var(--navy)" stroke-dasharray="24 151" transform="rotate(-90 30 30)"/>
      <circle cx="115" cy="30" r="24" stroke="var(--sand)"/><circle cx="115" cy="30" r="24" stroke="var(--navy)" stroke-dasharray="24 151" transform="rotate(-90 115 30)"/>
      <circle cx="205" cy="30" r="28" stroke="var(--sand)"/><circle cx="205" cy="30" r="28" stroke="var(--navy)" stroke-dasharray="28 176" transform="rotate(-90 205 30)"/>
      <circle cx="295" cy="30" r="24" stroke="var(--sand)"/><circle cx="295" cy="30" r="24" stroke="var(--navy)" stroke-dasharray="24 151" transform="rotate(-90 295 30)"/>
    </g>
    <g font-family="Montserrat,sans-serif" font-weight="700" font-size="10" fill="var(--navy)" text-anchor="middle">
      <text x="30" y="34">16%</text><text x="115" y="34">16%</text><text x="205" y="34">16%</text><text x="295" y="34">16%</text>
    </g>
  </svg>
  <p class="label" style="left:36px;top:144px">Lorem Ipsum Dolor</p><p class="label" style="left:120px;top:144px">Lorem Ipsum Dolor</p><p class="label" style="left:210px;top:144px">Lorem Ipsum Dolor</p><p class="label" style="left:300px;top:144px">Lorem Ipsum Dolor</p>
  <p class="body" style="left:36px;top:158px;width:66px">Short text explains this point.</p>
  <p class="body" style="left:120px;top:158px;width:66px">Short text explains this point.</p>
  <p class="body" style="left:210px;top:158px;width:66px">Short text explains this point.</p>
  <p class="body" style="left:300px;top:158px;width:66px">Short text explains this point.</p>
</section>
<section class="slide">
  <p class="title sm" style="left:140px;top:14px;width:120px;text-align:center">Your Business Presentation</p>
  <div class="letter sand" style="left:156px;top:62px;color:var(--navy)">S</div><div class="letter navy" style="left:204px;top:62px;color:var(--white)">W</div>
  <div class="letter navy" style="left:156px;top:122px;color:var(--white)">O</div><div class="letter sand" style="left:204px;top:122px;color:var(--navy)">T</div>
  <p class="label" style="left:36px;top:60px">Lorem Ipsum Dolor</p><p class="body" style="left:36px;top:72px;width:100px">Short supporting text explains this point.</p>
  <p class="label" style="left:36px;top:120px">Lorem Ipsum Dolor</p><p class="body" style="left:36px;top:132px;width:100px">Short supporting text explains this point.</p>
  <p class="label" style="left:270px;top:60px">Lorem Ipsum Dolor</p><p class="body" style="left:270px;top:72px;width:100px">Short supporting text explains this point.</p>
  <p class="label" style="left:270px;top:120px">Lorem Ipsum Dolor</p><p class="body" style="left:270px;top:132px;width:100px">Short supporting text explains this point.</p>
</section>

<!-- Row 15 -->
<section class="slide">
  <p class="title sm" style="left:100px;top:30px">Strengths</p>
  <div class="navy" style="left:0;top:50px;width:400px;height:80px"></div>
  <div class="letter" style="left:30px;top:70px;background:var(--beige);color:var(--navy)">S</div>
  <p class="label light" style="left:100px;top:60px">Lorem Ipsum Dolor</p><p class="label light" style="left:200px;top:60px">Lorem Ipsum Dolor</p><p class="label light" style="left:300px;top:60px">Lorem Ipsum Dolor</p>
  <p class="body light" style="left:100px;top:74px;width:80px">Short supporting text explains this point.</p>
  <p class="body light" style="left:200px;top:74px;width:80px">Short supporting text explains this point.</p>
  <p class="body light" style="left:300px;top:74px;width:80px">Short supporting text explains this point.</p>
  <div class="photo-wood" role="img" aria-label="Wooden staircase texture" style="left:0;top:130px;width:400px;height:95px"></div>
</section>
<section class="slide">
  <div class="navy" style="left:0;top:0;width:400px;height:120px"></div>
  <p class="title sm light" style="left:100px;top:20px">Weaknesses</p>
  <div class="letter" style="left:30px;top:56px;background:var(--beige);color:var(--navy)">W</div>
  <p class="label light" style="left:100px;top:50px">Lorem Ipsum Dolor</p><p class="label light" style="left:200px;top:50px">Lorem Ipsum Dolor</p><p class="label light" style="left:300px;top:50px">Lorem Ipsum Dolor</p>
  <p class="body light" style="left:100px;top:64px;width:80px">Short supporting text explains this point.</p>
  <p class="body light" style="left:200px;top:64px;width:80px">Short supporting text explains this point.</p>
  <p class="body light" style="left:300px;top:64px;width:80px">Short supporting text explains this point.</p>
  <div class="photo-wood" role="img" aria-label="Light wooden slatted wall" style="left:0;top:120px;width:400px;height:105px"></div>
</section>
<section class="slide">
  <div class="photo-city" role="img" aria-label="Office towers against blue sky" style="left:0;top:0;width:400px;height:100px"></div>
  <div class="navy" style="left:0;top:0;width:400px;height:10px"></div>
  <div class="letter" style="left:300px;top:80px;background:var(--navy);color:var(--white)">O</div>
  <p class="title sm" style="left:40px;top:128px">Opportunities</p>
  <p class="label" style="left:40px;top:150px">Lorem Ipsum Dolor</p><p class="label" style="left:150px;top:150px">Lorem Ipsum Dolor</p><p class="label" style="left:260px;top:150px">Lorem Ipsum Dolor</p>
  <p class="body" style="left:40px;top:164px;width:90px">Short supporting text explains this point.</p>
  <p class="body" style="left:150px;top:164px;width:90px">Short supporting text explains this point.</p>
  <p class="body" style="left:260px;top:164px;width:90px">Short supporting text explains this point.</p>
</section>

<!-- Row 16 -->
<section class="slide">
  <div class="photo-wood" role="img" aria-label="Wooden staircase in a bright room" style="left:0;top:0;width:400px;height:120px"></div>
  <div class="navy" style="left:0;top:120px;width:400px;height:105px"></div>
  <div class="letter" style="left:306px;top:96px;background:var(--beige);color:var(--navy)">T</div>
  <p class="title sm light" style="left:36px;top:126px">Threats</p>
  <p class="label light" style="left:36px;top:150px">Lorem Ipsum Dolor</p><p class="label light" style="left:146px;top:150px">Lorem Ipsum Dolor</p><p class="label light" style="left:256px;top:150px">Lorem Ipsum Dolor</p>
  <p class="body light" style="left:36px;top:164px;width:90px">Short supporting text explains this point.</p>
  <p class="body light" style="left:146px;top:164px;width:90px">Short supporting text explains this point.</p>
  <p class="body light" style="left:256px;top:164px;width:90px">Short supporting text explains this point.</p>
</section>
<section class="slide">
  <div class="photo-room" role="img" aria-label="Vase and shadows on a beige wall" style="left:0;top:0;width:400px;height:225px"></div>
  <div class="navy" style="left:210px;top:30px;width:150px;height:160px"></div>
  <p class="title sm light" style="left:210px;top:50px;width:150px;text-align:center">Add Your Title</p>
  <p class="body light" style="left:226px;top:90px;width:118px;text-align:center">Short supporting text explains this point for the audience.</p>
</section>
<section class="slide">
  <div class="photo-wood" role="img" aria-label="Wooden slatted wall" style="left:0;top:0;width:400px;height:90px"></div>
  <div class="photo-person portrait" role="img" aria-label="Portrait of presenter" style="left:168px;top:50px;width:64px;height:64px;border:3px solid var(--navy)"></div>
  <p class="title sm" style="left:0;top:124px;width:400px;text-align:center">Your Name</p>
  <p class="body" style="left:0;top:140px;width:400px;text-align:center">Description Here</p>
  <p class="body" style="left:80px;top:158px;width:240px;text-align:center">Short supporting text explains this point for the audience.</p>
  <span class="btn" style="left:170px;top:186px">www.website.com</span>
</section>

<!-- Row 17 -->
<section class="slide">
  <p class="title sm" style="left:34px;top:24px;width:120px">Your Business Presentation</p>
  <div class="photo-desk" role="img" aria-label="Person working at a laptop" style="left:0;top:80px;width:100px;height:100px"></div>
  <div class="navy" style="left:100px;top:80px;width:100px;height:100px"></div>
  <div class="photo-desk" role="img" aria-label="Woman at a desk with laptop" style="left:200px;top:80px;width:100px;height:100px"></div>
  <div class="navy" style="left:300px;top:80px;width:100px;height:100px"></div>
  <p class="label light" style="left:112px;top:96px">Add Title</p><p class="body light" style="left:112px;top:108px;width:78px">Short text explains this point.</p>
  <p class="label light" style="left:312px;top:96px">Add Title</p><p class="body light" style="left:312px;top:108px;width:78px">Short text explains this point.</p>
</section>
<section class="slide">
  <div class="photo-wood" role="img" aria-label="Room with wooden wall panels" style="left:0;top:0;width:400px;height:225px"></div>
  <div class="navy" style="left:150px;top:50px;width:180px;height:130px"></div>
  <p class="title sm light" style="left:168px;top:66px;width:120px">Your Business Presentation</p>
  <p class="body light" style="left:168px;top:104px;width:140px">Short supporting text explains this point for the audience.</p>
</section>
<section class="slide">
  <p class="title sm" style="left:30px;top:20px;width:100px">Add Your Title Here</p>
  <p class="body" style="left:30px;top:56px;width:140px">Short supporting text explains this point for the audience.</p>
  <div class="icon" style="left:30px;top:124px"></div><p class="label" style="left:62px;top:124px">Lorem Ipsum Dolor</p><p class="body" style="left:62px;top:134px;width:110px">Short text explains this point.</p>
  <div class="icon" style="left:30px;top:164px"></div><p class="label" style="left:62px;top:164px">Lorem Ipsum Dolor</p><p class="body" style="left:62px;top:174px;width:110px">Short text explains this point.</p>
  <div class="photo-room" role="img" aria-label="Bright office with desk and monitor" style="left:200px;top:0;width:200px;height:225px"></div>
  <svg style="left:280px;top:120px" width="120" height="105" viewBox="0 0 120 105"><polygon points="120,0 120,105 20,105" fill="var(--navy)"/></svg>
</section>

<!-- Row 18 -->
<section class="slide">
  <div class="photo-wood" role="img" aria-label="Wooden wall with bench" style="left:36px;top:36px;width:110px;height:150px"></div>
  <p class="title sm" style="left:200px;top:40px">Add Your Title</p><p class="body" style="left:200px;top:56px;width:170px">Short supporting text explains this point for the audience.</p>
  <p class="title sm" style="left:200px;top:120px">Add Your Title</p><p class="body" style="left:200px;top:136px;width:170px">Short supporting text explains this point for the audience.</p>
</section>
<section class="slide">
  <p class="title sm" style="left:20px;top:50px">Add Your Title</p>
  <p class="body" style="left:20px;top:74px;width:120px">Short supporting text explains this point for the audience. Short supporting text explains this point.</p>
  <div class="photo-room" role="img" aria-label="Vase with dried flowers and books" style="left:140px;top:24px;width:150px;height:170px"></div>
  <div class="photo-desk" role="img" aria-label="Man at a desk" style="left:300px;top:20px;width:90px;height:90px"></div>
  <div class="navy" style="left:300px;top:110px;width:90px;height:90px"></div>
  <p class="label light" style="left:310px;top:120px">Add Your Title</p><p class="body light" style="left:310px;top:132px;width:72px">Short text explains this point.</p>
</section>
<section class="slide">
  <p class="title sm" style="left:30px;top:30px;width:140px">Quote Lorem Ipsum Dolor sit Amet Consectu Labore et dolore magna</p>
  <p class="body" style="left:30px;top:110px;width:140px">Short supporting text explains this point for the audience.</p>
  <span class="btn" style="left:30px;top:170px">www.website.com</span>
  <div class="photo-desk" role="img" aria-label="Woman working at a laptop" style="left:220px;top:70px;width:90px;height:80px"></div>
  <div class="photo-room" role="img" aria-label="Bright room interior" style="left:310px;top:10px;width:90px;height:60px"></div>
  <div class="photo-room" role="img" aria-label="Interior with shelving" style="left:310px;top:160px;width:90px;height:65px"></div>
  <div class="icon" style="left:246px;top:20px;background:var(--white)"></div>
  <div class="icon" style="left:356px;top:100px;background:var(--white)"></div>
  <div class="icon" style="left:246px;top:172px;background:var(--white)"></div>
  <p class="body" style="left:220px;top:48px;width:80px">Short text explains this.</p>
</section>

<!-- Row 19 -->
<section class="slide">
  <p class="title sm" style="left:36px;top:20px;width:120px">Your Business Presentation</p>
  <p class="label" style="left:36px;top:66px">Lorem Ipsum Dolor</p><p class="body" style="left:36px;top:76px;width:140px">Short supporting text explains this point.</p>
  <p class="label" style="left:36px;top:110px">Lorem Ipsum Dolor</p><p class="body" style="left:36px;top:120px;width:140px">Short supporting text explains this point.</p>
  <svg style="left:240px;top:60px" width="130" height="140" viewBox="0 0 130 140">
    <g fill="var(--navy)"><rect x="8" y="30" width="10" height="90"/><rect x="40" y="50" width="10" height="70"/><rect x="72" y="20" width="10" height="100"/><rect x="104" y="40" width="10" height="80"/></g>
    <g font-family="Open Sans,sans-serif" font-size="6" fill="var(--ink)"><text x="4" y="132">2020</text><text x="36" y="132">2021</text><text x="68" y="132">2022</text><text x="100" y="132">2023</text></g>
  </svg>
</section>
<section class="slide">
  <svg style="left:30px;top:60px" width="130" height="140" viewBox="0 0 130 140">
    <g fill="var(--navy)"><rect x="8" y="50" width="12" height="70"/><rect x="40" y="20" width="12" height="100"/><rect x="72" y="40" width="12" height="80"/><rect x="104" y="10" width="12" height="110"/></g>
    <g font-family="Open Sans,sans-serif" font-size="6" fill="var(--ink)"><text x="4" y="132">2020</text><text x="36" y="132">2021</text><text x="68" y="132">2022</text><text x="100" y="132">2023</text></g>
  </svg>
  <p class="title sm" style="left:220px;top:20px;width:120px">Your Business Presentation</p>
  <p class="label" style="left:220px;top:66px">Lorem Ipsum Dolor</p><p class="body" style="left:220px;top:76px;width:150px">Short supporting text explains this point.</p>
  <p class="label" style="left:220px;top:110px">Lorem Ipsum Dolor</p><p class="body" style="left:220px;top:120px;width:150px">Short supporting text explains this point.</p>
</section>
<section class="slide">
  <p class="title sm" style="left:36px;top:20px;width:120px">Your Business Presentation</p>
  <p class="label" style="left:36px;top:66px">Lorem Ipsum Dolor</p><p class="body" style="left:36px;top:76px;width:130px">Short supporting text explains this point.</p>
  <p class="label" style="left:36px;top:110px">Lorem Ipsum Dolor</p><p class="body" style="left:36px;top:120px;width:130px">Short supporting text explains this point.</p>
  <svg style="left:210px;top:60px" width="170" height="130" viewBox="0 0 170 130">
    <g fill="var(--navy)"><rect x="30" y="4" width="120" height="8"/><rect x="30" y="28" width="90" height="8"/><rect x="30" y="52" width="140" height="8"/><rect x="30" y="76" width="70" height="8"/><rect x="30" y="100" width="110" height="8"/></g>
    <g font-family="Open Sans,sans-serif" font-size="6" fill="var(--ink)"><text x="0" y="11">2019</text><text x="0" y="35">2020</text><text x="0" y="59">2021</text><text x="0" y="83">2022</text><text x="0" y="107">2023</text></g>
  </svg>
</section>

<!-- Row 20 -->
<section class="slide">
  <p class="title sm" style="left:36px;top:20px;width:120px">Your Business Presentation</p>
  <p class="label" style="left:36px;top:66px">Lorem Ipsum Dolor</p><p class="body" style="left:36px;top:76px;width:140px">Short supporting text explains this point.</p>
  <p class="label" style="left:36px;top:110px">Lorem Ipsum Dolor</p><p class="body" style="left:36px;top:120px;width:140px">Short supporting text explains this point.</p>
  <svg style="left:230px;top:50px" width="150" height="140" viewBox="0 0 150 140">
    <polygon points="0,120 40,30 80,90 150,120" fill="var(--tan)"/><polygon points="40,120 100,40 150,120" fill="var(--navy)"/>
    <g font-family="Open Sans,sans-serif" font-size="6" fill="var(--ink)"><text x="-10" y="20">2022</text><text x="-10" y="80">2023</text></g>
  </svg>
</section>
<section class="slide">
  <p class="title sm" style="left:36px;top:20px;width:120px">Your Business Presentation</p>
  <p class="label" style="left:36px;top:66px">Lorem Ipsum Dolor</p><p class="body" style="left:36px;top:76px;width:140px">Short supporting text explains this point.</p>
  <p class="label" style="left:36px;top:110px">Lorem Ipsum Dolor</p><p class="body" style="left:36px;top:120px;width:140px">Short supporting text explains this point.</p>
  <svg style="left:220px;top:50px" width="160" height="140" viewBox="0 0 160 140">
    <path d="M0 40 C40 120 80 20 150 10" fill="none" stroke="var(--navy)" stroke-width="2"/>
    <path d="M10 70 C50 10 90 120 150 80" fill="none" stroke="var(--tan)" stroke-width="2"/>
    <text x="60" y="132" font-family="Open Sans,sans-serif" font-size="6" fill="var(--ink)">2023</text>
  </svg>
</section>
<section class="slide">
  <p class="title sm" style="left:36px;top:20px;width:120px">Your Business Presentation</p>
  <p class="label" style="left:36px;top:66px">Lorem Ipsum Dolor</p><p class="body" style="left:36px;top:76px;width:140px">Short supporting text explains this point.</p>
  <p class="label" style="left:36px;top:110px">Lorem Ipsum Dolor</p><p class="body" style="left:36px;top:120px;width:140px">Short supporting text explains this point.</p>
  <svg style="left:240px;top:50px" width="130" height="130" viewBox="0 0 130 130">
    <circle cx="65" cy="65" r="58" fill="var(--sand)"/><path d="M65 65 L65 7 A58 58 0 0 1 110 101 Z" fill="var(--navy)"/>
    <g font-family="Montserrat,sans-serif" font-weight="700" font-size="7"><text x="76" y="50" fill="#fff">2022</text><text x="30" y="80" fill="var(--navy)">2023</text></g>
  </svg>
</section>

<!-- Row 21 -->
<section class="slide">
  <div class="navy" style="left:0;top:0;width:400px;height:80px"></div>
  <p class="title sm light" style="left:34px;top:28px;width:120px">Your Business Presentation</p>
  <p class="body light" style="left:176px;top:34px;width:190px">Short supporting text explains this point for the audience.</p>
  <p class="label" style="left:70px;top:96px">Lorem Ipsum Dolor</p><p class="label" style="left:176px;top:96px">Lorem Ipsum Dolor</p><p class="label" style="left:282px;top:96px">Lorem Ipsum Dolor</p>
  <p class="body" style="left:70px;top:108px;width:80px">Short text explains this point.</p>
  <p class="body" style="left:176px;top:108px;width:80px">Short text explains this point.</p>
  <p class="body" style="left:282px;top:108px;width:80px">Short text explains this point.</p>
  <svg style="left:90px;top:140px" width="240" height="50" viewBox="0 0 240 50" fill="none" stroke="var(--navy)" stroke-width="6" stroke-linecap="round">
    <path d="M10 10 C20 40 60 40 80 30"/><path d="M72 22 L84 30 L72 38" stroke-width="3"/>
    <path d="M120 10 C130 40 170 40 190 30"/><path d="M182 22 L194 30 L182 38" stroke-width="3"/>
  </svg>
  <p class="label" style="left:70px;top:200px">Lorem Ipsum Dolor</p><p class="label" style="left:176px;top:200px">Lorem Ipsum Dolor</p><p class="label" style="left:282px;top:200px">Lorem Ipsum Dolor</p>
</section>
<section class="slide">
  <p class="title sm" style="left:26px;top:20px;width:120px">Your Business Presentation</p>
  <svg style="left:20px;top:90px" width="360" height="80" viewBox="0 0 360 80">
    <g fill="none" stroke-width="12">
      <path d="M10 70 A50 50 0 0 1 110 70" stroke="var(--navy)"/>
      <path d="M130 70 A50 50 0 0 1 230 70" stroke="var(--sand)"/><path d="M130 70 A50 50 0 0 1 160 26" stroke="var(--navy)"/>
      <path d="M250 70 A50 50 0 0 1 350 70" stroke="var(--sand)"/><path d="M250 70 A50 50 0 0 1 270 32" stroke="var(--navy)"/>
    </g>
    <g font-family="Montserrat,sans-serif" font-weight="700" font-size="11" fill="var(--navy)" text-anchor="middle">
      <text x="60" y="62">28.000</text><text x="180" y="62">10.000</text><text x="300" y="62">8000</text>
    </g>
  </svg>
  <p class="label" style="left:56px;top:176px">Lorem Ipsum Dolor</p><p class="label" style="left:176px;top:176px">Lorem Ipsum Dolor</p><p class="label" style="left:296px;top:176px">Lorem Ipsum Dolor</p>
  <p class="body" style="left:46px;top:188px;width:80px">Short text explains this point.</p>
  <p class="body" style="left:166px;top:188px;width:80px">Short text explains this point.</p>
  <p class="body" style="left:286px;top:188px;width:80px">Short text explains this point.</p>
</section>
<section class="slide">
  <p class="title sm" style="left:0;top:30px;width:400px;text-align:center">Free Icon 400+</p>
  <svg style="left:84px;top:64px" width="232" height="100" viewBox="0 0 232 100" fill="none" stroke="var(--navy)" stroke-width="1.4">
    <g><circle cx="8" cy="8" r="6"/><circle cx="32" cy="8" r="6"/><circle cx="56" cy="8" r="6"/><circle cx="80" cy="8" r="6"/><circle cx="104" cy="8" r="6"/><circle cx="128" cy="8" r="6"/><circle cx="152" cy="8" r="6"/><circle cx="176" cy="8" r="6"/><circle cx="200" cy="8" r="6"/><circle cx="224" cy="8" r="6"/></g>
    <g><circle cx="32" cy="32" r="6"/><circle cx="56" cy="32" r="6"/><circle cx="80" cy="32" r="6"/><circle cx="104" cy="32" r="6"/><circle cx="128" cy="32" r="6"/><circle cx="152" cy="32" r="6"/><circle cx="176" cy="32" r="6"/><circle cx="200" cy="32" r="6"/></g>
    <g><rect x="2" y="54" width="12" height="12"/><path d="M26 66 L32 54 L38 66Z"/><rect x="50" y="56" width="12" height="9"/><path d="M74 60 L86 60 M80 54 L80 66"/><circle cx="104" cy="60" r="6"/><path d="M122 60 L127 65 L134 55"/><path d="M146 60 L158 60 M153 55 L158 60 L153 65"/><rect x="170" y="54" width="12" height="12" rx="3"/><path d="M194 66 L200 54 L206 66"/><circle cx="224" cy="60" r="6"/></g>
    <g><path d="M26 84 L38 84 M32 78 L32 90"/><rect x="50" y="78" width="12" height="12"/><circle cx="80" cy="84" r="6"/><path d="M98 84 L103 89 L110 79"/><path d="M122 90 L128 78 L134 90Z"/><rect x="146" y="79" width="12" height="10"/><path d="M170 84 L182 84 M177 79 L182 84 L177 89"/><circle cx="200" cy="84" r="6"/></g>
  </svg>
</section>

</main>
</body>
</html>
```